die Packwerker
diePackwerker
Sehr professionelle und schnelle Bearbeitung. Lief alle wie erhofft und wir hoffen auch zukünftig zusammen arbeiten zu können.
Zielgruppe
Wir sind nicht irgendeine Umzugsfirma, wir sind „die Packwerker“
Aufgabenstellung
Die Daten bitte von der der Website entnehmen. diepackwerker.bayern
Hinten sollte ein Gutschein mit drauf. (57€) Kann auch komplett geändert werden.
diepackwerker.bayern

```html
<!DOCTYPE html>
<html lang="de">
<head>
<meta charset="utf-8">
<title>die Packwerker – Visitenkarte und Gutschein</title>
<link href="https://fonts.googleapis.com/css2?family=Open+Sans:wght@300;400;700&display=swap" rel="stylesheet">
<style>
  :root {
    --page-bg: #e9e9e7;
    --card-white: #ffffff;
    --voucher-blue: #2fa8e0;
    --brand-red: #d3182a;
    --brand-blue: #2a9fd8;
    --text-grey: #3c3c3c;
    --text-white: #ffffff;
  }
  * { box-sizing: border-box; margin: 0; padding: 0; }
  html, body { width: 1200px; height: 873px; overflow: hidden; }
  body {
    background: var(--page-bg);
    font-family: "Open Sans", sans-serif;
    display: flex;
    align-items: center;
    justify-content: center;
    gap: 40px;
  }
  .card {
    position: relative;
    width: 540px;
    height: 350px;
    box-shadow: 0 6px 18px rgba(0,0,0,0.18);
  }
  .card::after {
    content: "";
    position: absolute;
    inset: 8px;
    border: 2px solid var(--brand-red);
    pointer-events: none;
  }
  .card-front { background: var(--card-white); }
  .card-back { background: var(--voucher-blue); }

  .front-content {
    position: absolute;
    left: 150px;
    top: 52px;
    color: var(--text-grey);
  }
  .brand {
    display: flex;
    align-items: center;
    gap: 12px;
    margin-bottom: 18px;
  }
  .brand-dot {
    width: 34px; height: 34px;
    border-radius: 50%;
    background: var(--brand-red);
  }
  .brand-name {
    font-size: 30px;
    font-weight: 700;
    color: var(--brand-blue);
    letter-spacing: -0.5px;
  }
  .website { font-size: 17px; font-weight: 300; margin-bottom: 8px; }
  .person { font-size: 20px; color: var(--brand-red); margin-bottom: 8px; }
  .contact-line {
    display: flex;
    align-items: center;
    gap: 10px;
    font-size: 17px;
    font-weight: 300;
    margin-bottom: 6px;
  }
  .contact-icon { width: 18px; height: 18px; flex: none; }

  .back-content {
    position: absolute;
    left: 36px; right: 36px; top: 30px;
    color: var(--text-white);
  }
  .voucher-title {
    font-size: 52px;
    font-weight: 700;
    color: var(--brand-red);
    text-align: right;
    line-height: 1.05;
    margin-bottom: 18px;
    padding-right: 10px;
  }
  .voucher-text { font-size: 13.5px; font-weight: 300; line-height: 1.6; }
  .voucher-web { color: var(--brand-red); font-size: 14px; margin-top: 2px; }
  .voucher-fine {
    font-size: 7.5px;
    font-weight: 300;
    line-height: 1.45;
    margin-top: 26px;
  }
</style>
</head>
<body>
  <section class="card card-front">
    <div class="front-content">
      <div class="brand">
        <span class="brand-dot"></span>
        <span class="brand-name">die Packwerker</span>
      </div>
      <p class="website">diepackwerker.bayern</p>
      <p class="person">Marek Holzner</p>
      <p class="contact-line">
        <svg class="contact-icon" viewBox="0 0 24 24"><path fill="#2a9fd8" d="M6.6 10.8a15 15 0 0 0 6.6 6.6l2.2-2.2a1 1 0 0 1 1-.25 11.4 11.4 0 0 0 3.6.57 1 1 0 0 1 1 1V20a1 1 0 0 1-1 1A17 17 0 0 1 3 4a1 1 0 0 1 1-1h3.5a1 1 0 0 1 1 1c0 1.25.2 2.45.57 3.57a1 1 0 0 1-.25 1z"/></svg>
        08947215038
      </p>
      <p class="contact-line">
        <svg class="contact-icon" viewBox="0 0 24 24"><path fill="#2a9fd8" d="M6.6 10.8a15 15 0 0 0 6.6 6.6l2.2-2.2a1 1 0 0 1 1-.25 11.4 11.4 0 0 0 3.6.57 1 1 0 0 1 1 1V20a1 1 0 0 1-1 1A17 17 0 0 1 3 4a1 1 0 0 1 1-1h3.5a1 1 0 0 1 1 1c0 1.25.2 2.45.57 3.57a1 1 0 0 1-.25 1z"/></svg>
        015762931047
      </p>
      <p class="contact-line">
        <svg class="contact-icon" viewBox="0 0 24 24"><rect x="2" y="4" width="20" height="16" fill="#2a9fd8"/><path d="M3 5l9 8 9-8M3 19l7-6M21 19l-7-6" stroke="#fff" stroke-width="1.6" fill="none"/></svg>
        info@diepackwerker.bayern
      </p>
    </div>
  </section>

  <section class="card card-back">
    <div class="back-content">
      <h1 class="voucher-title">Gutschein 57€</h1>
      <p class="voucher-text">
        Sie können den Gutschein gleich bei Ihrem nächsten Umzug bei uns einlösen.*<br>
        Einfach beim Umzug Ihrem Team-Leiter vorzeigen!<br>
        Der Gutschein ist nicht Personengebunden, somit auch als Geschenk verwendbar.<br>
        Um unseres Unternehmen besser kennen zu lernen besuchen Sie uns in Internet.
      </p>
      <p class="voucher-web">www.diepackwerker.bayern</p>
      <p class="voucher-fine">
        *Nur gültig bei Abruf unserer Umzugsleistungen bei einem Rechnungswert ab 399 Euro. Nicht einlösbar für Kauf von Verpackungsmaterial sowie Lagerung. Pro Umzug ist die Einlösung nur eines Gutscheins möglich. Gültig bis zum 31.12.2016
      </p>
    </div>
  </section>
</body>
</html>
```